Unique Home Cooking School needs Wordpress Design

We need a wordpress design for our small business based in Singapore called Brisk Ladles. It is a unique cooking school where the cooking course menu is completely customised to our client's preference/lifestyle/requests. More information can be found on our site: briskladles.example

We are looking for something simple and easy to navigate. We are currently using a free template which we have customised ourselves. As the business is growing, we are looking to have a site more suited to our needs. The site should also be photo friendly, as we often post up photos of our food. It should also be social media integrated as a lot of our business is driven by PQ.

The look and feel should really reflect the personalities of both owners - like the logo. Please feel free to contact us if you need more clarification.

Target Market(s)

Our target audience are usually female, with children, aged 25 - 45.
They are either stay-at-home mums or full-time mums that are keen to do more for the family.

Industry/Entity Type

Small Business

Requirements
Must have
• The wordpress design has to be able to accommodate food photos on every page.
It also needs to be able to support social media feeds within the site.
Should not have
• Design should not have any chef-like design elements as we are not chefs. We are two stay-home-mums wanting to impart skills to other stay-home-mums or domestic helpers.

```html
<!DOCTYPE html>
<html lang="en">
<head>
<meta charset="utf-8">
<title>Brisk Ladles – Contact Us</title>
<link href="https://fonts.googleapis.com/css2?family=Arimo:wght@400;700&family=Open+Sans:ital,wght@0,400;0,600;0,700;1,400;1,600&family=Libre+Baskerville&display=swap" rel="stylesheet">
<style>
:root{
  --peach:#f8c4ae;
  --peach-text:#f5b89c;
  --navy:#1f3a6e;
  --ink:#111;
  --grey-text:#444;
  --field:#f1f1f1;
  --field-line:#cfcfcf;
  --panel:#f2f2f2;
  --dark:#231f20;
  --footer:#3d434b;
  --rule:#c9c9c9;
}
*{box-sizing:border-box;margin:0;padding:0}
html,body{width:972px;height:1200px;overflow:hidden;background:#fff}
body{position:relative;font-family:"Arimo",Arial,sans-serif;color:var(--ink)}
.abs{position:absolute}

/* navigation */
.main-nav{left:147px;top:16px;display:flex;gap:22px;font-size:9px;letter-spacing:.5px}
.main-nav a{color:#222;text-decoration:none;position:relative}
.main-nav a.active::after{content:"";position:absolute;left:50%;top:15px;margin-left:-3px;border:3px solid transparent;border-top:4px solid var(--peach)}
.social-dots{right:147px;top:15px;display:flex;gap:9px}
.social-dots span{width:11px;height:11px;border-radius:50%;background:var(--peach)}

/* header band */
.header-band{left:0;top:42px;width:972px;height:167px;background:radial-gradient(ellipse at 30% 50%,#efefef,#dcdcdc)}
.brand{left:147px;top:150px;width:172px;text-align:center}
.brand-name{font-family:"Open Sans",sans-serif;font-size:22px;color:#222;line-height:1}
.brand-tag{font-family:"Libre Baskerville",serif;font-size:7px;color:#222;margin-top:6px}
.hero-photo{left:386px;top:42px;width:439px;height:167px;background:linear-gradient(120deg,#6d5a45 0%,#3a2a1f 35%,#2b1d15 60%,#8a4a1e 85%,#c76a25 100%)}
.hero-caption{left:386px;top:119px;width:234px;height:59px;background:rgba(0,0,0,.82);color:#fff;padding:6px 10px}
.hero-caption h1{font-size:24px;font-weight:700;line-height:1.1}
.hero-caption p{font-size:10px;margin-top:3px}

/* contact form */
.field{background:var(--field);border:1px solid var(--field-line);font-family:"Open Sans",sans-serif;font-size:10px;color:#666;padding:8px 12px}
.captcha{left:160px;top:467px;font-family:"Open Sans",sans-serif;font-weight:700;font-size:14px;letter-spacing:4px}
.btn{background:var(--peach);font-size:10px;color:#222;display:flex;align-items:center;justify-content:center;box-shadow:0 2px 2px rgba(0,0,0,.18)}

/* contact details */
.double-rule{height:4px;border-top:1px solid var(--navy);border-bottom:1px solid var(--navy)}
.detail{width:222px;text-align:center;font-family:"Open Sans",sans-serif;font-size:15px;line-height:1.1}
.detail h3{color:var(--peach-text);font-size:14px;font-weight:700}

/* social + reviews */
.like-panel{left:148px;top:738px;width:226px;height:166px;background:var(--panel)}
.like-panel h2{position:absolute;left:17px;top:14px;font-family:"Open Sans",sans-serif;font-size:15px;color:var(--navy);font-weight:700}
.page-thumb{left:17px;top:36px;width:28px;height:28px;background:#fff;border:1px solid #ddd}
.page-name{left:52px;top:37px;font-family:"Open Sans",sans-serif;font-size:9px;color:#3b5998}
.like-badge{left:53px;top:51px;width:26px;height:10px;background:#4267b2}
.panel-rule{left:17px;top:71px;width:192px;border-top:1px solid #999}
.photo-grid{left:18px;top:82px;display:grid;grid-template-columns:repeat(6,29px);grid-auto-rows:29px;gap:1px 0}
.reviews{left:386px;top:738px;width:439px;height:166px;background:var(--dark)}
.reviews h2{position:absolute;left:13px;top:14px;font-family:"Open Sans",sans-serif;font-size:14px;color:#fff;font-weight:700}
.quote{left:17px;top:40px;width:405px;height:97px;background:var(--peach);padding:13px 10px 0 14px;font-family:"Open Sans",sans-serif;font-style:italic;font-size:9px;line-height:17px;color:#111}
.quote-tail{left:37px;top:137px}
.author{left:58px;top:143px;font-family:"Open Sans",sans-serif;font-style:italic;font-weight:600;font-size:9px;color:#fff}

/* footer columns */
.col-head{font-family:"Open Sans",sans-serif;font-size:14px;font-weight:700;color:#111;border-bottom:1px solid var(--rule);padding-bottom:2px}
.about-text{left:150px;top:997px;width:288px;font-size:7.6px;line-height:13.5px;color:var(--grey-text)}
.connect-item{left:460px;display:flex;align-items:center;gap:12px;font-size:8.6px;line-height:1.15;color:#222}
.ring{width:29px;height:29px;border:1.5px solid #111;border-radius:50%}
.sub-note{left:619px;top:994px;font-size:8px;color:#333}
.sub-field{width:207px;height:23px;border:1px solid #aaa;font-size:8px;color:#333;padding:6px 11px;background:#fff}
.page-rule{left:147px;top:1150px;width:678px;border-top:1px solid #bbb}
.site-footer{left:0;top:1166px;width:972px;height:34px;background:var(--footer)}
.copyright{left:147px;top:21px;font-size:8px;color:#fff}
</style>
</head>
<body>

<nav class="abs main-nav">
  <a href="#">HOME</a><a href="#">ABOUT US</a><a href="#">COURESE</a><a href="#">BLOG</a><a href="#" class="active">CONTACT US</a>
</nav>
<div class="abs social-dots"><span></span><span></span><span></span></div>

<header>
  <div class="abs header-band"></div>
  <div class="abs brand">
    <div class="brand-name">Brisk Ladles</div>
    <div class="brand-tag">Cooking Lessons for Everyone</div>
  </div>
  <div class="abs hero-photo" role="img" aria-label="Photo of freshly dug carrots and garden tools in dark soil"></div>
  <div class="abs hero-caption">
    <h1>Contact Us</h1>
    <p>Cooking Lessons for Everyone</p>
  </div>
</header>

<form class="contact-form">
  <div class="abs field" style="left:158px;top:248px;width:155px;height:28px">Your Name</div>
  <div class="abs field" style="left:325px;top:248px;width:155px;height:28px">Your Email</div>
  <div class="abs field" style="left:492px;top:248px;width:155px;height:28px">Your Contact Number</div>
  <div class="abs field" style="left:659px;top:248px;width:155px;height:28px">Subject</div>
  <div class="abs field" style="left:158px;top:292px;width:656px;height:155px;padding-top:10px">Your Message</div>
  <div class="abs captcha">FP8D</div>
  <div class="abs field" style="left:228px;top:464px;width:103px;height:22px"></div>
  <div class="abs btn" style="left:337px;top:464px;width:74px;height:22px">Send</div>
</form>

<section class="contact-details">
  <div class="abs double-rule" style="left:147px;top:542px;width:222px"></div>
  <div class="abs double-rule" style="left:375px;top:542px;width:222px"></div>
  <div class="abs double-rule" style="left:603px;top:542px;width:222px"></div>
  <div class="abs detail" style="left:147px;top:573px"><h3>Physcial</h3>Brisk Ladles Cooking<br>Lessons for Everyone</div>
  <div class="abs detail" style="left:375px;top:574px"><h3>Email us:</h3>info@briskladles.example</div>
  <div class="abs detail" style="left:603px;top:574px"><h3>Phone:</h3>+65.8000.1234<br>+65.9000.5678</div>
  <div class="abs double-rule" style="left:147px;top:653px;width:222px"></div>
  <div class="abs double-rule" style="left:375px;top:653px;width:222px"></div>
  <div class="abs double-rule" style="left:603px;top:653px;width:222px"></div>
</section>

<section class="abs like-panel">
  <h2>Like on PQ</h2>
  <div class="abs page-thumb"></div>
  <div class="abs page-name">Brisk Ladles</div>
  <div class="abs like-badge"></div>
  <div class="abs panel-rule"></div>
  <div class="abs photo-grid" role="img" aria-label="Grid of follower profile photos">
    <div style="background:#8a5a45"></div><div style="background:#2b4a8a"></div><div style="background:#9a7f6a"></div><div style="background:#8a5a45"></div><div style="background:#2b4a8a"></div><div style="background:#a88570"></div>
    <div style="background:#1d4f8f"></div><div style="background:#b8bcc0"></div><div style="background:#eef3e6"></div><div style="background:#1d4f8f"></div><div style="background:#b8bcc0"></div><div style="background:#eef3e6"></div>
  </div>
</section>

<section class="abs reviews">
  <h2>Customer Reviews</h2>
  <div class="abs quote">Lorem Ipsum has been the industry's standard dummy text ever since the 1500s, when an unknown printer took a galley of type and scrambled it to make a type specimen book. It has survived not only five centuries, but also the leap into electronic typesetting, remaining essentially unchanged. It was popularised in the 1960s with the release of Transfera sheets containing.</div>
  <svg class="abs quote-tail" width="18" height="17" viewBox="0 0 18 17"><polygon points="0,0 18,0 0,17" fill="#f8c4ae"/></svg>
  <div class="abs author">Author - 1</div>
</section>

<section class="footer-columns">
  <div class="abs col-head" style="left:149px;top:953px;width:288px">About Us</div>
  <p class="abs about-text">We are two very Brisk Ladles who share a passion for cooking and eating different foods, trying out new eateries and the love for collecting cookbooks! We believe that eating well and being able to provide our young families with delicious, healthy meals made at home is the foundation to general well-being.&nbsp; Since being Mums and whenever possible we try to make a lot from scratch to ensure only good things go into our children's bodies. From mushy baby foods, to healthy sweet or savoury snacks to enticing meals that will interest them enough to eat it!</p>

  <div class="abs col-head" style="left:459px;top:953px;width:134px">Connect With Us</div>
  <div class="abs connect-item" style="top:995px"><span class="ring"></span><span>Find us On<br>PQ</span></div>
  <div class="abs connect-item" style="top:1036px"><span class="ring"></span><span>Find us On<br>Chirrup</span></div>
  <div class="abs connect-item" style="top:1076px"><span class="ring"></span><span>Find us On<br>Pinboardly</span></div>

  <div class="abs col-head" style="left:617px;top:953px;width:210px">Get Latest updates</div>
  <div class="abs sub-note">Subscribe to Get our latest news</div>
  <div class="abs sub-field" style="left:619px;top:1018px">Name</div>
  <div class="abs sub-field" style="left:619px;top:1046px">Your Email Address</div>
  <div class="abs btn" style="left:619px;top:1080px;width:74px;height:22px">Subscribe</div>
</section>

<div class="abs page-rule"></div>
<footer class="abs site-footer">
  <div class="abs copyright">Copyright © 2014 Brisk Ladles.</div>
</footer>

</body>
</html>
```